E-Book-Cover-Design für Selfpublisherin
Vielen Dank für das schöne Design und die professionelle Zusammenarbeit.
Zielgruppe
Ich bin selfpublisherin und suche ein Cover für das neue ebook. Bei dem derzeitigen Projekt handelt es sich um eine Liebesgeschichte, die im Irland der heutigen Zeit spielt.
Zielgruppe sind Frauen verschiedenen Alters.
Aufgabenstellung
Titel des Buches ist: 'Ein Sommer voller Zufall'
Das Ganze soll unter dem Pseudonym 'Hester Quinby' veröffentlicht werden.
Es soll deutlich werden, dass es sich um eine leichte Lektüre handelt, wie man sie gerne mit in den Urlaub nehmen würde. Die Geschichte hat lustige Elemente, insgesamt aber einen ruhigen Grundton, ohne außerordentlich viel Ironie.

```html
<!DOCTYPE html>
<html lang="de">
<head>
<meta charset="utf-8">
<title>Ein Sommer voller Zufall – Hester Quinby</title>
<link rel="stylesheet" href="https://fonts.googleapis.com/css2?family=Merriweather:wght@400;700&family=Kaushan+Script&family=Barlow+Semi+Condensed:wght@600&display=swap">
<style>
  :root {
    --page: #ffffff;
    --title-blue: #0b3d7e;
    --author-white: #ffffff;
    --sky-top: #f3f5f8;
    --sky-low: #e4ebf1;
    --horizon: #dfe6ea;
    --sea: #5f8ea3;
    --sea-deep: #3f6f86;
    --grass: #7e9a3c;
    --grass-deep: #66812d;
  }
  * { margin: 0; padding: 0; box-sizing: border-box; }
  html, body {
    width: 848px; height: 1200px; overflow: hidden;
    background: var(--page);
  }
  .canvas { position: relative; width: 848px; height: 1200px; background: var(--page); }
  .cover {
    position: absolute; left: 121px; top: 133px;
    width: 602px; height: 963px; overflow: hidden;
  }
  .cover-photo {
    position: absolute; inset: 0;
    background: linear-gradient(180deg,
      var(--sky-top) 0%,
      var(--sky-low) 40%,
      var(--horizon) 47%,
      var(--sea) 50%,
      var(--sea-deep) 62%,
      var(--grass) 72%,
      var(--grass-deep) 100%);
  }
  .title { position: absolute; inset: 0; color: var(--title-blue); font-weight: normal; }
  .title-top {
    position: absolute; left: 183px; top: 72px;
    font-family: "Merriweather", Georgia, serif;
    font-weight: 700; font-size: 60px; line-height: 1; letter-spacing: 0.5px;
  }
  .title-mid {
    position: absolute; left: 440px; top: 152px;
    font-family: "Merriweather", Georgia, serif;
    font-weight: 400; font-size: 29px; line-height: 1;
  }
  .title-main {
    position: absolute; left: 40px; top: 200px; width: 520px;
    text-align: center;
    font-family: "Kaushan Script", cursive;
    font-size: 150px; line-height: 1;
  }
  .author {
    position: absolute; left: 0; right: 0; top: 893px;
    text-align: center; padding-left: 16px;
    font-family: "Barlow Semi Condensed", "Arial Narrow", sans-serif;
    font-weight: 600; font-size: 34px; letter-spacing: 1px;
    color: var(--author-white);
  }
</style>
</head>
<body>
<main class="canvas">
  <section class="cover">
    <div class="cover-photo" role="img" aria-label="Foto: Frau in pinker Jacke mit Rucksack sitzt auf einer grünen Klippe an der irischen Küste und blickt auf das Meer unter hellem Himmel"></div>
    <h1 class="title">
      <span class="title-top">Ein Sommer</span>
      <span class="title-main">Zufall</span>
      <span class="title-mid">voller</span>
    </h1>
    <p class="author">HESTER QUINBY</p>
  </section>
</main>
</body>
</html>
```